QuilloBrezza Business cards

Dear team, I need to get the design file to suit it to our team. The focus of the business card is the Automotive Market and the design must be in black colour and the logo must be in glossy black. On the front of the card I need to get the following info:

- Name and Surname
- Title
- eMail
- Phone Number
- Skype account
- domain address

```html
<!DOCTYPE html>
<html lang="en">
<head>
<meta charset="UTF-8">
<title>QuilloBrezza Business Card</title>
<link rel="stylesheet" href="https://fonts.googleapis.com/css2?family=Poppins:wght@700&family=Arimo:wght@400&display=swap">
<style>
  :root {
    --stage: #2e2f31;
    --card: #ffffff;
    --navy: #0b1033;
    --navy-deep: #0a0f3a;
    --navy-soft: #1a2470;
    --red: #ec2f38;
    --ink: #111111;
    --light: #f2f3f7;
  }
  * { margin: 0; padding: 0; box-sizing: border-box; }
  html, body { width: 1200px; height: 900px; overflow: hidden; background: var(--stage); }
  .stage { position: relative; width: 1200px; height: 900px; }

  .card {
    position: absolute; left: 250px;
    width: 700px; height: 400px;
    border-radius: 18px; overflow: hidden;
  }
  .card-front { top: 40px; background: var(--card); }
  .card-back { top: 460px; background: var(--navy-deep); }

  .card-band { position: absolute; inset: 0; }
  .brand {
    position: absolute; left: 47px; top: 32px;
    display: flex; align-items: center; gap: 11px;
  }
  .brand-dot { width: 30px; height: 30px; border-radius: 50%; background: var(--red); }
  .brand-name {
    font-family: "Poppins", sans-serif; font-weight: 700;
    font-size: 39px; color: var(--red); letter-spacing: -0.5px;
  }
  .person { position: absolute; left: 47px; top: 146px; }
  .person-name {
    font-family: "Poppins", sans-serif; font-weight: 700;
    font-size: 27px; color: var(--red); letter-spacing: 0.5px; line-height: 1.1;
  }
  .person-title {
    font-family: "Arimo", sans-serif; font-size: 16px; color: var(--light); margin-top: 3px;
  }
  .contact-list { list-style: none; margin-top: 9px; }
  .contact-item {
    display: flex; align-items: center; gap: 7px;
    font-family: "Arimo", sans-serif; font-size: 16px; color: var(--light);
    line-height: 1.3;
  }
  .contact-icon { width: 12px; height: 12px; flex: none; }
  .address {
    position: absolute; left: 27px; top: 338px;
    font-family: "Arimo", sans-serif; font-size: 17px; color: var(--ink);
  }
  .wheel-mark {
    position: absolute; left: 481px; top: 203px;
    width: 153px; height: 153px; border-radius: 50%;
    background: var(--red); border: 7px solid var(--card);
  }

  .back-pattern {
    position: absolute; inset: 0;
    background: linear-gradient(135deg, var(--navy-deep) 0%, var(--navy-soft) 50%, var(--navy-deep) 100%);
  }
  .back-brand {
    position: absolute; right: 34px; bottom: 28px;
    display: flex; align-items: center; gap: 9px;
  }
  .back-brand-dot { width: 22px; height: 22px; border-radius: 50%; background: var(--red); }
  .back-brand-name {
    font-family: "Poppins", sans-serif; font-weight: 700;
    font-size: 24px; color: var(--red);
  }
</style>
</head>
<body>
<main class="stage">
  <article class="card card-front">
    <svg class="card-band" viewBox="0 0 700 400" width="700" height="400" aria-hidden="true">
      <polygon points="0,123 700,123 700,353 0,293" fill="var(--navy)"/>
    </svg>

    <div class="brand">
      <span class="brand-dot"></span>
      <span class="brand-name">QuilloBrezza.com</span>
    </div>

    <section class="person">
      <h1 class="person-name">DARREN COLE</h1>
      <p class="person-title">Director</p>
      <ul class="contact-list">
        <li class="contact-item">
          <svg class="contact-icon" viewBox="0 0 24 24"><path fill="var(--red)" d="M6.6 10.8a15 15 0 0 0 6.6 6.6l2.2-2.2a1 1 0 0 1 1-.25 11.4 11.4 0 0 0 3.6.57 1 1 0 0 1 1 1V20a1 1 0 0 1-1 1A17 17 0 0 1 3 4a1 1 0 0 1 1-1h3.5a1 1 0 0 1 1 1c0 1.25.2 2.45.57 3.57a1 1 0 0 1-.25 1z"/></svg>
          555-014-2288
        </li>
        <li class="contact-item">
          <svg class="contact-icon" viewBox="0 0 24 24"><rect x="2" y="5" width="20" height="14" rx="2" fill="var(--red)"/><path d="M3 6l9 7 9-7" fill="none" stroke="var(--navy)" stroke-width="2"/></svg>
          info@quillobrezza.com
        </li>
        <li class="contact-item">
          <svg class="contact-icon" viewBox="0 0 24 24"><circle cx="12" cy="12" r="10" fill="var(--red)"/></svg>
          quillobrezza
        </li>
      </ul>
    </section>

    <p class="address">4120 N Alder, Fenwick, Oregon 97201</p>

    <div class="wheel-mark" role="img" aria-label="Brand wheel emblem area"></div>
  </article>

  <article class="card card-back">
    <div class="back-pattern" role="img" aria-label="Embossed repeating brand pattern in deep navy"></div>
    <div class="back-brand">
      <span class="back-brand-dot"></span>
      <span class="back-brand-name">QuilloBrezza</span>
    </div>
  </article>
</main>
</body>
</html>
```